TalkBridge - Language Coaching Services

Sleek, innovative, trendy design for Language Coaching business.

TalkBridge is a new UK based company that provides Language Coaching services. We offer highly personalized on-line and face to face language courses. We also impart learning techniques workshops based on the latest neuroscience research for second-language acquisition.

Target Market(s)

Industry/Entity Type

Consulting

Contact Information for Business Card

TalkBridge
ElenaVT@talkbridge-demo.co.uk
TalkBridge-demo.co.uk
London, UK

Font styles to use
Sans Serif

```html
<!DOCTYPE html>
<html lang="en">
<head>
<meta charset="utf-8">
<title>TalkBridge – Business Card</title>
<link rel="stylesheet" href="https://fonts.googleapis.com/css2?family=Lato:wght@400;700;900&display=swap">
<style>
  :root {
    --page-bg: #eceef0;
    --card-bg: #f7f8f9;
    --brand-blue: #0b7dba;
    --brand-blue-deep: #006fab;
    --brand-blue-soft: #2a8fc6;
    --text-light: #ffffff;
  }
  html, body {
    margin: 0;
    width: 1200px;
    height: 900px;
    overflow: hidden;
    background: var(--page-bg);
    font-family: "Lato", Arial, sans-serif;
  }
  .business-card {
    position: absolute;
    left: 150px;
    top: 180px;
    width: 900px;
    height: 540px;
    background: var(--card-bg);
    overflow: hidden;
    box-shadow: 0 10px 30px rgba(0,0,0,0.12);
  }
  .blue-panel {
    position: absolute;
    left: 0;
    top: 0;
    width: 560px;
    height: 540px;
  }
  .contact-block {
    position: absolute;
    left: 48px;
    top: 180px;
    color: var(--text-light);
  }
  .person-name {
    margin: 0;
    font-weight: 900;
    font-size: 31px;
    letter-spacing: 0.5px;
    line-height: 1.1;
  }
  .person-role {
    margin: 2px 0 0;
    font-size: 25px;
    line-height: 1.2;
  }
  .location {
    margin: 28px 0 0 3px;
    font-size: 25px;
  }
  .contact-list {
    list-style: none;
    margin: 28px 0 0 3px;
    padding: 0;
    font-size: 25px;
    line-height: 33px;
  }
  .contact-list li {
    display: flex;
    align-items: center;
    gap: 8px;
  }
  .contact-icon {
    width: 20px;
    height: 20px;
    flex: none;
  }
  .brand-mark {
    position: absolute;
    left: 560px;
    top: 260px;
    width: 300px;
    display: flex;
    flex-direction: column;
    align-items: center;
  }
  .brand-dot {
    width: 130px;
    height: 130px;
    border-radius: 50%;
    background: var(--brand-blue);
  }
  .brand-name {
    margin-top: 26px;
    font-size: 54px;
    font-weight: 700;
    color: var(--brand-blue);
    letter-spacing: 1px;
  }
</style>
</head>
<body>
  <div class="business-card">
    <svg class="blue-panel" viewBox="0 0 560 540" role="img" aria-label="Blue head-profile silhouette illustration">
      <path d="M0 0 H340 C470 0 540 150 540 300 C540 430 480 510 430 540 H0 Z" fill="var(--brand-blue-soft)"/>
      <path d="M0 0 H270 C420 0 510 140 510 300 C510 420 460 500 410 540 H0 Z" fill="var(--brand-blue-deep)"/>
    </svg>

    <div class="contact-block">
      <h1 class="person-name">DANIEL CARTER</h1>
      <p class="person-role">Managing Director</p>
      <p class="location">London, UK</p>
      <ul class="contact-list">
        <li>
          <svg class="contact-icon" viewBox="0 0 20 20"><rect x="5" y="1" width="10" height="18" rx="2" fill="none" stroke="#fff" stroke-width="2"/><circle cx="10" cy="15.5" r="1.2" fill="#fff"/></svg>
          044 777 1234
        </li>
        <li>
          <svg class="contact-icon" viewBox="0 0 20 20"><rect x="1" y="4" width="18" height="12" fill="#fff"/><path d="M1 4 L10 11 L19 4" fill="none" stroke="var(--brand-blue-deep)" stroke-width="1.5"/></svg>
          ElenaVT@talkbridge-demo.co.uk
        </li>
        <li>
          <svg class="contact-icon" viewBox="0 0 20 20"><circle cx="10" cy="10" r="8.5" fill="#fff"/><path d="M10 1.5 V18.5 M1.5 10 H18.5 M10 1.5 C5 6 5 14 10 18.5 M10 1.5 C15 6 15 14 10 18.5" fill="none" stroke="var(--brand-blue-deep)" stroke-width="1.2"/></svg>
          www.TalkBridge-demo.co.uk
        </li>
      </ul>
    </div>

    <div class="brand-mark">
      <div class="brand-dot"></div>
      <div class="brand-name">TalkBridge</div>
    </div>
  </div>
</body>
</html>
```